A Freight forwarding (transportation/shipping) company requires stationary designs

We need The following:
1. Letterhead
2. Letter Envelope
3. Business Card Design
4. A4 Paper Envelope
5. A4 Paper Folder (One that is 2xA4 foldable size which we can open in half and we can put a paper in between and has a lot for business card)
6. A5 Paper (To be used for notes taking)
a design for a freight forwarding company named KORVELA MIND INTERNATIONAL TRANSPORTATION.
(We are active in Sea Transportation, Truck transportation, and Air Transportation, (printed design in PDF is required with all open source files for editing - lamination accepted)
Playing around with the Logo is accepted,, Korvela Logo.png is the correct logo.
Example of folder, envelopes, and notepad attached
Address of the company is :
No 7, 4th Tarandil Gharbi, Neshat Lar Blvd,
Mashhad, IR
Tel : +98 51 37412958
Fax : +98 51 37490316
Website : www.korvela-example.com
Email : info@korvela-example.com

```html
<!DOCTYPE html>
<html lang="en">
<head>
<meta charset="utf-8">
<title>Korvela Mind – Letterhead</title>
<link href="https://fonts.googleapis.com/css2?family=Arimo:ital,wght@0,400;0,700;1,400&display=swap" rel="stylesheet">
<style>
  :root {
    --navy: #2a3a8c;
    --blue: #0b4f9e;
    --green: #2f9a45;
    --ink: #2b2b2b;
    --muted: #6f6f6f;
    --paper: #ffffff;
    --stage: #e9e9e9;
    --pattern-a: #f4f4f4;
    --pattern-b: #e6e6e6;
  }
  * { box-sizing: border-box; margin: 0; padding: 0; }
  html, body { width: 1200px; height: 720px; overflow: hidden; }
  body {
    background: var(--stage);
    font-family: "Arimo", Arial, sans-serif;
    color: var(--ink);
    position: relative;
  }
  .sheet {
    position: absolute;
    top: 50px;
    width: 424px;
    height: 600px;
    background: var(--paper);
    overflow: hidden;
  }
  .sheet--front { left: 150px; }
  .sheet--back { left: 626px; }

  .brand {
    display: flex;
    align-items: center;
    justify-content: center;
    gap: 6px;
    color: var(--navy);
    font-weight: 700;
    letter-spacing: 0.04em;
  }
  .brand__dot {
    border-radius: 50%;
    background: var(--navy);
    flex: none;
  }
  .sheet--front .brand { margin-top: 34px; font-size: 13px; }
  .sheet--front .brand__dot { width: 12px; height: 12px; }

  .letter { padding: 34px 46px 0 54px; font-size: 7px; line-height: 1.38; }
  .recipient { margin-bottom: 16px; }
  .recipient__name { font-weight: 700; }
  .letter__body p { text-align: justify; margin-bottom: 9px; }
  .letter__closing { margin-top: 6px; }
  .signature { margin-top: 34px; }
  .signature__name { font-weight: 700; }
  .signature__role { font-style: italic; }

  .footer-wave { position: absolute; left: 0; bottom: 0; width: 424px; height: 90px; }

  .pattern {
    position: absolute; inset: 0;
    background: linear-gradient(180deg, var(--pattern-a), var(--pattern-b));
  }
  .sheet--back .brand {
    position: absolute; left: 0; right: 0; top: 280px;
    font-size: 16px;
  }
  .sheet--back .brand__dot { width: 14px; height: 14px; }

  .caption {
    position: absolute;
    top: 662px;
    width: 424px;
    text-align: center;
    font-size: 11px;
    letter-spacing: 0.12em;
    color: var(--muted);
  }
  .caption--front { left: 150px; }
  .caption--back { left: 626px; }
</style>
</head>
<body>
  <section class="sheet sheet--front" aria-label="Letterhead front">
    <div class="brand"><span class="brand__dot"></span>KORVELA MIND</div>

    <article class="letter">
      <div class="recipient">
        <div class="recipient__name">Mr. Daniel Reyes</div>
        <div>Managing Director</div>
        <div>USA Investor</div>
        <div>42 Harbor Lane</div>
        <div>USA</div>
      </div>
      <div class="letter__body">
        <p>Lorem ipsum dolor sit amet, consectetuer adipiscing elit. Nam cursus. Morbi ut mi. Nullam enim leo, egestas id, condimentum at, laoreet mattis, massa. Sed eleifend nonummy diam. Praesent mauris ante, elementum et, bibendum at, posuere sit amet, nibh. Duis tincidunt lectus quis dui viverra vestibulum.</p>
        <p>Suspendisse vulputate aliquam dui. Nulla elementum dui ut augue. Aliquam vehicula mi at mauris. Maecenas placerat, nisl at consequat rhoncus, sem nunc gravida justo, quis eleifend arcu velit quis lacus. Morbi magna magna, tincidunt a, mattis non, imperdiet vitae, tellus. Sed odio est, auctor ac, sollicitudin in, consequat vitae, orci. Fusce id felis. Vivamus sollicitudin metus eget eros.</p>
        <p>Metus eget eros. Pellentesque habitant morbi tristique senectus et netus et malesuada fames ac turpis egestas. In posuere felis nec tortor. Pellentesque faucibus. Ut accumsan ultricies elit. Maecenas at justo id velit placerat molestie. Donec dictum lectus non odio. Cras a ante vitae enim iaculis aliquam.</p>
        <p>Mauris nunc quam, venenatis nec, euismod sit amet, egestas placerat, est. Pellentesque habitant morbi tristique senectus et netus et malesuada fames ac turpis egestas. Cras id elit. Integer quis urna. Ut ante enim, dapibus malesuada, fringilla eu, condimentum quis, tellus. Aenean porttitor eros vel dolor. Donec convallis pede venenatis nibh. Duis quam.</p>
      </div>
      <p class="letter__closing">Thank you for being one of our valued customers.</p>
      <div class="signature">
        <div class="signature__name">Name Here</div>
        <div class="signature__role">CEO</div>
      </div>
    </article>

    <svg class="footer-wave" viewBox="0 0 424 90" aria-hidden="true">
      <path d="M0 40 C 120 10, 240 10, 424 30 L424 44 C 250 22, 130 24, 0 52 Z" fill="var(--green)"/>
      <path d="M0 46 C 130 18, 250 18, 424 38 L424 90 L0 90 Z" fill="var(--blue)"/>
    </svg>
  </section>

  <section class="sheet sheet--back" aria-label="Letterhead back">
    <div class="pattern" role="img" aria-label="Faint repeating pattern of small arched emblem motifs covering the page"></div>
    <div class="brand"><span class="brand__dot"></span>KORVELA MIND</div>
  </section>

  <div class="caption caption--front">Letterhead Front</div>
  <div class="caption caption--back">Letterhead Back</div>
</body>
</html>
```